Etiketten-Design für Weinflasche
Sehr gute Zusammenarbeit bei Tag und Nacht, sehr kooperativ ,flexibel und entgegenkommend. Empfehlenswert
Zielgruppe
Weinbau - Eigenbau Wein -Weinverkauf
Aufgabenstellung
Bräuchte oder Suche ein Flaschenetikette für Rotwein der Marke Zweigelt Das Ausmaß der Etikette sollte 8cm Breit und 12cm Hoch sein. Habe meine letzte Etikette beigelegt sie Anhang

```html
<!DOCTYPE html>
<html lang="de">
<head>
<meta charset="utf-8">
<title>Zweigelt 2020 – Flaschenetikett</title>
<link rel="stylesheet" href="https://fonts.googleapis.com/css2?family=Roboto+Condensed:wght@300;400&display=swap">
<style>
  :root {
    --stage: #e8e5e1;
    --label-dark: #25292a;
    --band: #323536;
    --body: #474747;
    --year: #6a6c6d;
    --text-light: #d6d6d6;
    --wordmark: #9a9c9d;
    --wine-red: #7a1410;
  }
  * { margin: 0; padding: 0; box-sizing: border-box; }
  html, body {
    width: 816px;
    height: 1200px;
    overflow: hidden;
    background: var(--stage);
    font-family: "Roboto Condensed", "Arial Narrow", sans-serif;
  }
  .label {
    position: absolute;
    left: 88px;
    top: 120px;
    width: 640px;
    height: 960px;
    background: var(--body);
    overflow: hidden;
  }
  .label-head {
    position: absolute;
    left: 0; top: 0;
    width: 640px;
    height: 212px;
    background: var(--band);
    display: flex;
  }
  .brand {
    width: 236px;
    height: 212px;
    background: var(--label-dark);
    display: flex;
    flex-direction: column;
    align-items: center;
    justify-content: center;
    gap: 14px;
  }
  .brand-dot {
    width: 64px;
    height: 64px;
    border-radius: 50%;
    background: var(--wine-red);
  }
  .brand-name {
    font-weight: 300;
    font-size: 21px;
    letter-spacing: 0.5px;
    color: var(--wordmark);
    text-transform: uppercase;
  }
  .vintage {
    flex: 1;
    font-weight: 300;
    font-size: 212px;
    line-height: 212px;
    letter-spacing: -4px;
    color: var(--year);
    text-align: center;
    overflow: hidden;
  }
  .pattern {
    position: absolute;
    left: 0; top: 212px;
    width: 640px;
    height: 748px;
    background: linear-gradient(180deg, #4a4a4a 0%, #444444 100%);
  }
  .wine-info {
    position: absolute;
    left: 0;
    top: 560px;
    width: 640px;
    text-align: center;
    color: var(--text-light);
    text-transform: uppercase;
    font-weight: 300;
  }
  .variety {
    font-size: 56px;
    letter-spacing: 1px;
    line-height: 1;
    margin-bottom: 34px;
  }
  .producer, .region {
    font-size: 30px;
    line-height: 1.2;
  }
</style>
</head>
<body>
  <main class="label">
    <div class="pattern" role="img" aria-label="Dezentes Ornamentmuster aus Weinranken und Trauben in Grautönen"></div>
    <header class="label-head">
      <div class="brand">
        <span class="brand-dot"></span>
        <span class="brand-name">Martin Tolvanek</span>
      </div>
      <div class="vintage">2020</div>
    </header>
    <section class="wine-info">
      <h1 class="variety" style="font-weight:300">Zweigelt</h1>
      <p class="producer">Martin Tolvanek Weinbau</p>
      <p class="region">Burgenland</p>
    </section>
  </main>
</body>
</html>
```